Selka Marven Photography Business Card

I need a new business card/ possibly design to use for other marking materials ... I have included my logo below in a few different colors, but can also provide the logo in additional colors and sizes. I would love a card the expresses clean, simple and classy.

Target Market(s)

Portrait photography clients, child photography clients

Industry/Entity Type

Photographer

Contact Information for Business Card

Selka Marven Photography, Willowmere MA, www.selkamarvenphotography-demo.com
T. 555-203-1946 E. selkamarvenphoto@mailbox-demo.com

Colors
33b8a4
eea4c8
5c5c5c

Requirements
Must have
• I would like to include my logo on card.
Nice to have
• I also like the color brown as well as the choices below. I would like a simple, elegant card, something classy.

```html
<!DOCTYPE html>
<html lang="en">
<head>
<meta charset="utf-8">
<title>Selka Marven Photography Business Card</title>
<link rel="stylesheet" href="https://fonts.googleapis.com/css2?family=Lato:wght@400;700&display=swap">
<style>
  :root {
    --bg: #e9e7e4;
    --paper: #ffffff;
    --crimson: #a8282b;
    --blush: #f2a9c6;
    --shadow: rgba(40, 30, 25, 0.18);
  }
  * { margin: 0; padding: 0; box-sizing: border-box; }
  html, body {
    width: 1200px; height: 800px; overflow: hidden;
    background: var(--bg);
    font-family: "Lato", Arial, sans-serif;
  }
  .stage {
    width: 1200px; height: 800px;
    display: flex; flex-direction: column; align-items: center; justify-content: center;
    gap: 50px;
  }
  .card {
    position: relative;
    width: 610px; height: 348px;
    box-shadow: 0 10px 26px var(--shadow);
  }
  .card--front { background: var(--paper); color: var(--crimson); }
  .card--back { background: var(--crimson); color: var(--blush); }

  .viewfinder { position: absolute; inset: 0; width: 100%; height: 100%; }

  .brand {
    position: absolute; left: 0; right: 0; top: 112px;
    text-align: center;
    font-weight: 700; font-size: 30px; letter-spacing: 0.5px;
  }

  .contact-row {
    position: absolute; left: 42px; right: 42px; top: 212px;
    display: flex; justify-content: space-between; align-items: center;
    font-size: 14px;
  }
  .contact-item { display: flex; align-items: center; gap: 7px; white-space: nowrap; }
  .contact-item svg { width: 13px; height: 13px; fill: currentColor; flex: none; }

  .web-rule {
    position: absolute; left: 0; right: 0;
    display: flex; align-items: center; gap: 16px;
    font-size: 19px; white-space: nowrap;
  }
  .card--front .web-rule { top: 262px; }
  .card--back .web-rule { top: 270px; }
  .web-rule::before, .web-rule::after {
    content: ""; flex: 1; height: 2px; background: currentColor;
  }
</style>
</head>
<body>
<main class="stage">

  <section class="card card--front" aria-label="Card front">
    <svg class="viewfinder" viewBox="0 0 610 348" aria-hidden="true">
      <g fill="none" stroke="var(--crimson)" stroke-width="5">
        <path d="M150 84 V70 H164"/>
        <path d="M446 70 H460 V84"/>
        <path d="M150 168 V182 H164"/>
        <path d="M446 182 H460 V168"/>
      </g>
    </svg>
    <div class="brand">Selka Marven Photography</div>
    <div class="contact-row">
      <span class="contact-item">
        <svg viewBox="0 0 24 24"><path d="M6.6 10.8a15.1 15.1 0 0 0 6.6 6.6l2.2-2.2a1 1 0 0 1 1-.25 11.4 11.4 0 0 0 3.6.57 1 1 0 0 1 1 1V20a1 1 0 0 1-1 1A17 17 0 0 1 3 4a1 1 0 0 1 1-1h3.5a1 1 0 0 1 1 1c0 1.250.2 2.450.57 3.570a1 1 0 0 1-.25 1z"/></svg>
        555-203-1946
      </span>
      <span class="contact-item">
        <svg viewBox="0 0 24 24"><path d="M12 2a7 7 0 0 0-7 7c0 5.2 7 13 7 13s7-7.8 7-13a7 7 0 0 0-7-7zm0 9.5A2.5 2.5 0 1 1 12 6.5a2.5 2.5 0 0 1 0 5z"/></svg>
        Willowmere MA
      </span>
      <span class="contact-item">
        <svg viewBox="0 0 24 24"><path d="M3 5h18a1 1 0 0 1 1 1v12a1 1 0 0 1-1 1H3a1 1 0 0 1-1-1V6a1 1 0 0 1 1-1zm9 7.2L4.5 7.3v1.9L12 14l7.5-4.8V7.3z"/></svg>
        selkamarvenphoto@mailbox-demo.com
      </span>
    </div>
    <div class="web-rule">www.selkamarvenphotography-demo.com</div>
  </section>

  <section class="card card--back" aria-label="Card back">
    <svg class="viewfinder" viewBox="0 0 610 348" aria-hidden="true">
      <g fill="none" stroke="var(--blush)" stroke-width="5">
        <path d="M150 84 V70 H164"/>
        <path d="M446 70 H460 V84"/>
        <path d="M150 168 V182 H164"/>
        <path d="M446 182 H460 V168"/>
      </g>
    </svg>
    <div class="brand">Selka Marven Photography</div>
    <div class="web-rule">www.selkamarvenphotography-demo.com</div>
  </section>

</main>
</body>
</html>
```